Design some Business Cards

We are a Photography and Social Media company that takes pictures for business and individuals and creates Loopmarket, Pixelwharf, Chirrel etc. We need a very creative business card that has our logo. We will be getting our business cards from norda stamp. We don't have a set location yet so the address can be 457 fenwick lane Brooklyn NY 10987. phone number xxx-xxx-xxxx

Please find our logo attached.

Please incorporate both logos.

Please have both logos on separate sides of the business card.

```html
<!DOCTYPE html>
<html lang="en">
<head>
<meta charset="utf-8">
<title>Bright Frame Studio – Business Card</title>
<link rel="stylesheet" href="https://fonts.googleapis.com/css2?family=Roboto:wght@400;500;700&display=swap">
<style>
  :root {
    --backdrop: #d9dcde;
    --card-dark: #1c1c1c;
    --card-light: #ffffff;
    --ink-light: #ffffff;
    --ink-dark: #2b2b2b;
    --ink-mid: #3a3a3a;
    --accent-grey: #8c8a88;
  }
  html, body {
    margin: 0;
    padding: 0;
    width: 1200px;
    height: 1200px;
    overflow: hidden;
    background: var(--backdrop);
  }
  .canvas {
    position: relative;
    width: 1200px;
    height: 1200px;
  }
  .card {
    position: absolute;
    left: 233px;
    width: 737px;
    height: 442px;
    border-radius: 14px;
    box-shadow: 0 6px 18px rgba(0,0,0,0.25);
    overflow: hidden;
  }
  .card--front { top: 131px; background: var(--card-dark); }
  .card--back  { top: 627px; background: var(--card-light); }

  .brand {
    position: absolute;
    display: flex;
    align-items: center;
    justify-content: center;
    gap: 16px;
    margin: 0;
    font-family: "Roboto", sans-serif;
    font-weight: 400;
    white-space: nowrap;
  }
  .brand__mark {
    flex: none;
    border-radius: 50%;
    background: var(--accent-grey);
  }

  .card--front .brand {
    left: 0; right: 0; top: 192px;
    height: 60px;
    color: var(--ink-light);
    font-size: 46px;
  }
  .card--front .brand__mark { width: 26px; height: 26px; }

  .front__url {
    position: absolute;
    left: 0; right: 0; top: 383px;
    margin: 0;
    text-align: center;
    font-family: "Roboto", sans-serif;
    font-size: 20px;
    letter-spacing: 4px;
    color: var(--ink-light);
  }

  .card--back .brand {
    left: 395px; width: 330px; top: 198px;
    height: 46px;
    color: var(--ink-dark);
    font-size: 31px;
    gap: 12px;
  }
  .card--back .brand__mark { width: 20px; height: 20px; }

  .contact {
    position: absolute;
    left: 24px; top: 100px;
    font-family: "Roboto", sans-serif;
    color: var(--ink-mid);
  }
  .contact__name {
    margin: 0;
    font-size: 27px;
    font-weight: 700;
    line-height: 30px;
  }
  .contact__role {
    margin: 0;
    font-size: 20px;
    font-weight: 500;
    line-height: 22px;
  }
  .contact__company {
    margin: 30px 0 0;
    font-size: 19px;
    line-height: 24px;
  }
  .contact__list {
    list-style: none;
    margin: 30px 0 0;
    padding: 0;
    font-size: 18px;
  }
  .contact__item {
    display: flex;
    align-items: center;
    height: 27px;
  }
  .contact__icon {
    width: 20px; height: 20px;
    margin-right: 14px;
    fill: var(--ink-mid);
  }
</style>
</head>
<body>
<main class="canvas">

  <section class="card card--front" aria-label="Card front">
    <h1 class="brand">
      <span class="brand__mark" aria-hidden="true"></span>
      Bright Frame Studio
    </h1>
    <p class="front__url">www.brightframe.com</p>
  </section>

  <section class="card card--back" aria-label="Card back">
    <div class="contact">
      <p class="contact__name">ELMER TOVEY</p>
      <p class="contact__role">CEO &amp; Founder</p>
      <p class="contact__company">Bright Frame Studio:-<br>457 fenwick lane Brooklyn NY 10987</p>
      <ul class="contact__list">
        <li class="contact__item">
          <svg class="contact__icon" viewBox="0 0 24 24" aria-hidden="true"><path d="M6.6 10.8a15.1 15.1 0 0 0 6.6 6.6l2.2-2.2a1 1 0 0 1 1-.25 11.4 11.4 0 0 0 3.6.57 1 1 0 0 1 1 1V20a1 1 0 0 1-1 1A17 17 0 0 1 3 4a1 1 0 0 1 1-1h3.5a1 1 0 0 1 1 1c0 1.25.2 2.450.57 3.57a1 1 0 0 1-.25 1z"/></svg>
          xxx-xxx-xxxx
        </li>
        <li class="contact__item">
          <svg class="contact__icon" viewBox="0 0 24 24" aria-hidden="true"><path d="M2 5h20v14H2z M4 7v.5l8 5 8-5V7z" fill-rule="evenodd"/></svg>
          elmer@brightframe.com
        </li>
        <li class="contact__item">
          <svg class="contact__icon" viewBox="0 0 24 24" aria-hidden="true"><path d="M12 2a10 10 0 1 0 0 20 10 10 0 0 0 0-20zm-1 17.9A8 8 0 0 1 4.1 11H7v2l2 2v2l2 1zm6.9-2.5A2 2 0 0 0 16 16h-1v-3a1 1 0 0 0-1-1H8v-2h2a1 1 0 0 0 1-1V7h2a2 2 0 0 0 2-2v-.4a8 8 0 0 1 2.9 12.8z"/></svg>
          www.brightframe.com
        </li>
      </ul>
    </div>
    <p class="brand">
      <span class="brand__mark" aria-hidden="true"></span>
      Bright Frame Studio
    </p>
  </section>

</main>
</body>
</html>
```